BARRIER BANNER OTP

I am looking for a visual for a banner
3 meters long by 1 high.
In the same theme as the visual identity of the company.
As simple as possible without overloading

There must be the LOGO, the title TECHNIQUE SERVICES ROUSSEL

_________________________

I am looking for a visual for a banner (barrier banner)
3 meters long by 1 high.

AIR CONDITIONING HEATING VENTILATION
04 52 31 64 19

Font styles to use
Sans Serif

Colors
33b8a4
00a990
33a6d7
0493ce
3176b5
0355a3
ffffff

Requirements
Should not have
• No photo
No photo

```html
<!DOCTYPE html>
<html lang="fr">
<head>
<meta charset="utf-8">
<title>OTP – Barrier banner samples</title>
<link rel="stylesheet" href="https://fonts.googleapis.com/css2?family=Montserrat:wght@600;700;800&display=swap">
<style>
  :root {
    --sheet: #a3a3a3;
    --ink: #2f3d48;
    --white: #ffffff;
    --green: #45cc87;
    --teal: #33a6a8;
    --blue: #2a8fc6;
    --brand-gradient: linear-gradient(90deg, var(--green) 0%, var(--teal) 55%, var(--blue) 100%);
  }
  * { box-sizing: border-box; margin: 0; padding: 0; }
  html, body { width: 1075px; height: 1200px; overflow: hidden; }
  body {
    background: var(--sheet);
    font-family: "Montserrat", "Helvetica Neue", Arial, sans-serif;
    position: relative;
  }
  .sample-label {
    position: absolute; left: 53px;
    transform: translate(-50%, -50%) rotate(-90deg);
    color: var(--white); font-size: 11px; font-weight: 600; letter-spacing: .5px;
    white-space: nowrap;
  }
  .banner {
    position: absolute; left: 76px; width: 938px; height: 313px;
    overflow: hidden; box-shadow: 0 2px 6px rgba(0,0,0,.25);
  }
  .banner-top { position: absolute; left: 0; top: 0; width: 100%; height: 234px; }
  .banner-bottom { position: absolute; left: 0; top: 234px; width: 100%; height: 79px; }
  .top-light { background: var(--white); }
  .top-dark { background: var(--ink); }
  .bottom-gradient { background: var(--brand-gradient); }
  .bottom-dark { background: var(--ink); }
  .bottom-light { background: var(--white); }

  .brand-mark {
    position: absolute; display: flex; align-items: flex-end; gap: 12px;
    font-weight: 800; line-height: .8; letter-spacing: 2px;
  }
  .brand-mark .dot { width: 26px; height: 26px; background: var(--teal); margin-bottom: 4px; }
  .brand-dark { color: var(--ink); }
  .brand-light { color: var(--white); }

  .divider { position: absolute; width: 1px; }
  .company-name { position: absolute; font-weight: 800; white-space: nowrap; }

  .title-block { position: absolute; left: 432px; width: 490px; top: 38px; text-align: center; }
  .title-block h1 { font-size: 37px; font-weight: 800; line-height: 39px; color: var(--ink); letter-spacing: .3px; }
  .title-rule { width: 148px; height: 2px; margin: 18px auto 16px; background: linear-gradient(90deg, transparent, var(--blue) 15%, var(--blue) 85%, transparent); }
  .title-block p { font-size: 29px; font-weight: 800; line-height: 32px; color: var(--blue); }

  .service-panel {
    position: absolute; left: 526px; top: 62px; width: 412px; height: 128px;
    background: var(--brand-gradient);
    display: flex; align-items: center; justify-content: center; text-align: center;
    color: var(--white); font-size: 36px; font-weight: 800; line-height: 38px;
  }

  .phone-icon { position: absolute; left: 37px; top: 13px; width: 26px; height: 51px; }
  .phone-number {
    position: absolute; left: 75px; top: 8px;
    font-size: 58px; font-weight: 800; letter-spacing: -1px; line-height: 62px; white-space: nowrap;
  }
  .number-light { color: var(--white); text-shadow: 3px 3px 0 #111; }
  .number-dark { color: var(--ink); }

  .web-pill {
    position: absolute; top: 18px; right: 0; height: 40px;
    border-radius: 20px 0 0 20px;
    display: flex; align-items: center; gap: 8px; padding-left: 8px;
    font-size: 22px; font-weight: 700; white-space: nowrap;
  }
  .pill-light { left: 493px; background: var(--white); color: var(--ink); }
  .pill-gradient { left: 488px; background: var(--brand-gradient); color: var(--white); }
  .web-pill svg { width: 28px; height: 28px; flex: none; }
</style>
</head>
<body>

<!-- Sample 1 -->
<span class="sample-label" style="top:352px">SAMPLE 1</span>
<section class="banner" style="top:71px">
  <div class="banner-top top-light">
    <div class="brand-mark brand-dark" style="left:58px; top:62px; font-size:150px;">OTP<span class="dot"></span></div>
    <div class="divider" style="left:416px; top:38px; height:176px; background:var(--ink);"></div>
    <div class="title-block">
      <h1>TECHNIQUE SERVICES<br>ROUSSEL</h1>
      <div class="title-rule"></div>
      <p>AIR CONDITIONING<br>HEATING VENTILATION</p>
    </div>
  </div>
  <div class="banner-bottom bottom-gradient">
    <svg class="phone-icon" viewBox="0 0 26 51"><rect x="1.5" y="1.5" width="23" height="48" rx="3" fill="none" stroke="#fff" stroke-width="3"/><rect x="4" y="7" width="18" height="34" fill="#fff"/><circle cx="13" cy="45" r="2" fill="#fff"/></svg>
    <div class="phone-number number-light">04 52 31 64 19</div>
    <div class="web-pill pill-light">
      <svg viewBox="0 0 28 28"><g fill="none" stroke="#2a8fc6" stroke-width="2"><circle cx="14" cy="14" r="12"/><ellipse cx="14" cy="14" rx="5.5" ry="12"/><path d="M2 14h24M4 8h20M4 20h20M14 2v24"/></g></svg>
      technique-services-roussel.fr
    </div>
  </div>
</section>

<!-- Sample 2 -->
<span class="sample-label" style="top:722px">SAMPLE 2</span>
<section class="banner" style="top:444px">
  <div class="banner-top top-light">
    <div class="brand-mark brand-dark" style="left:112px; top:48px; font-size:140px;">OTP<span class="dot"></span></div>
    <div class="company-name" style="left:40px; top:186px; font-size:24px; color:var(--ink);">TECHNIQUE SERVICES ROUSSEL</div>
    <div class="divider" style="left:525px; top:38px; height:175px; background:var(--ink);"></div>
    <div class="service-panel">AIR CONDITIONING<br>HEATING<br>VENTILATION</div>
  </div>
  <div class="banner-bottom bottom-dark">
    <svg class="phone-icon" viewBox="0 0 26 51"><rect x="1.5" y="1.5" width="23" height="48" rx="3" fill="none" stroke="#fff" stroke-width="3"/><rect x="4" y="7" width="18" height="34" fill="#2f3d48"/><circle cx="13" cy="45" r="2" fill="#fff"/></svg>
    <div class="phone-number number-light">04 52 31 64 19</div>
    <div class="web-pill pill-light">
      <svg viewBox="0 0 28 28"><g fill="none" stroke="#2a8fc6" stroke-width="2"><circle cx="14" cy="14" r="12"/><ellipse cx="14" cy="14" rx="5.5" ry="12"/><path d="M2 14h24M4 8h20M4 20h20M14 2v24"/></g></svg>
      technique-services-roussel.fr
    </div>
  </div>
</section>

<!-- Sample 3 -->
<span class="sample-label" style="top:1094px">SAMPLE 2</span>
<section class="banner" style="top:816px">
  <div class="banner-top top-dark">
    <div class="brand-mark brand-light" style="left:112px; top:48px; font-size:140px;">OTP<span class="dot"></span></div>
    <div class="company-name" style="left:40px; top:186px; font-size:24px; color:var(--white);">TECHNIQUE SERVICES ROUSSEL</div>
    <div class="divider" style="left:525px; top:38px; height:175px; background:var(--green);"></div>
    <div class="service-panel">AIR CONDITIONING<br>HEATING<br>VENTILATION</div>
  </div>
  <div class="banner-bottom bottom-light">
    <svg class="phone-icon" viewBox="0 0 26 51"><rect x="0" y="0" width="26" height="51" rx="4" fill="#45cc87"/><rect x="4" y="7" width="18" height="34" fill="#fff"/><circle cx="13" cy="45" r="2" fill="#fff"/></svg>
    <div class="phone-number number-dark">04 52 31 64 19</div>
    <div class="web-pill pill-gradient">
      <svg viewBox="0 0 28 28"><g fill="none" stroke="#fff" stroke-width="2"><circle cx="14" cy="14" r="12"/><ellipse cx="14" cy="14" rx="5.5" ry="12"/><path d="M2 14h24M4 8h20M4 20h20M14 2v24"/></g></svg>
      technique-services-roussel.fr
    </div>
  </div>
</section>

</body>
</html>
```